ATM BUSINESS MACHINES...

NEED A NEW LOGO AND BUSINESS CARD FOR A BRAND NEW ATM BUSINESS. WE GO TO LOCAL BUSINESSES AND PLACE ATM'S IN THER STORES FOR FREE. IT INCREASES THEIR BUSINESS. A VERY EYE CATCHY LOGO AND COLOR SCHEME...MODERN, PROFESSIONAL, YET MODERN AND APPEALING....

Target Market(s)

alll types of business owners...young & old....

Industry/Entity Type

Business

Contact Information for Business Card

PALMETTO QUICK FUNDS-ATM'S
" GET YOUR CASH NOW"
Ray T. Holbrook
President/Owner
P.O. Box 87
Hollow Pines, S.C. 29872
pqf.atm@zentromail.com
Free Atm's- Free Instalation, Free Maintenance Never a cost to business owner......Call now to get you free ATM and increase your sales......

Requirements
Nice to have
• $$$ signs.....colors....raised letters....
Maybe a logo PQF $$$ with ATM machine...

```html
<!DOCTYPE html>
<html lang="en">
<head>
<meta charset="utf-8">
<title>Palmetto Quick Funds – Business Card</title>
<link rel="stylesheet" href="https://fonts.googleapis.com/css2?family=Fira+Sans:ital,wght@0,600;1,700&family=Jost:ital,wght@0,300;0,400;0,500;1,400&display=swap">
<style>
  :root {
    --bg-deep: #020807;
    --bg-glow: #0a3a33;
    --green: #4cbf5a;
    --lime: #9ccc3a;
    --orange: #f6a232;
    --white: #f2f2f2;
    --grey: #e4e4e4;
  }
  * { margin: 0; padding: 0; box-sizing: border-box; }
  html, body { width: 1200px; height: 702px; overflow: hidden; background: var(--bg-deep); }
  .card {
    position: relative;
    width: 1200px; height: 702px;
    background: radial-gradient(ellipse 720px 520px at 560px 0px, var(--bg-glow) 0%, #06201c 40%, var(--bg-deep) 85%);
    font-family: "Jost", sans-serif;
    color: var(--white);
  }
  .brand {
    position: absolute; left: 100px; top: 258px; width: 436px;
    text-align: center;
  }
  .brand-name {
    font-family: "Jost", sans-serif;
    font-weight: 400;
    font-size: 52px;
    letter-spacing: 1px;
    line-height: 1;
    color: var(--white);
    white-space: nowrap;
  }
  .brand-rule {
    height: 5px; margin: 22px 0 0 13px; width: 407px;
    background: linear-gradient(90deg, var(--lime), var(--green));
  }
  .brand-tagline {
    margin-top: 10px;
    font-size: 31px; line-height: 1.2; color: var(--white);
    white-space: nowrap;
  }
  .brand-tagline em { font-style: italic; }
  .brand-tagline .dot { margin: 0 16px; font-size: 20px; vertical-align: middle; }
  .call-to-action {
    position: absolute; left: 110px; top: 494px; width: 400px;
    text-align: center;
    font-family: "Fira Sans", sans-serif; font-weight: 600;
    font-size: 28px; line-height: 37px; letter-spacing: 0.6px;
    color: var(--orange);
  }
  .divider {
    position: absolute; left: 602px; top: 68px; width: 5px; height: 548px;
    background: linear-gradient(180deg, var(--green), var(--lime) 50%, var(--green));
  }
  .offers {
    position: absolute; left: 640px; top: 96px; width: 500px;
    text-align: center;
    font-family: "Fira Sans", sans-serif; font-weight: 600;
    font-size: 30px; line-height: 51px; letter-spacing: 1.5px;
    color: var(--white);
  }
  .offers .free { color: var(--green); }
  .offers .no-cost { font-style: italic; font-weight: 700; font-size: 28px; letter-spacing: 0.5px; }
  .contact { position: absolute; left: 649px; top: 410px; }
  .contact-name {
    font-family: "Fira Sans", sans-serif; font-weight: 600;
    font-size: 27px; line-height: 34px; letter-spacing: 0.8px; color: var(--orange);
  }
  .contact-title {
    font-family: "Fira Sans", sans-serif; font-weight: 600;
    font-size: 27px; line-height: 34px; letter-spacing: 0.5px; color: var(--white);
  }
  .contact-details {
    margin-top: 14px;
    display: grid; grid-template-columns: 126px auto;
    font-size: 27px; line-height: 33px; color: var(--grey); font-weight: 400;
  }
</style>
</head>
<body>
<main class="card">
  <section class="brand">
    <div class="brand-name">palmetto quick funds</div>
    <div class="brand-rule"></div>
    <div class="brand-tagline">ATMs<span class="dot">•</span><em>Get your cash now!</em></div>
  </section>

  <p class="call-to-action">Call (555) 010-4477<br>to get your FREE ATM<br>&amp; increase your sales!</p>

  <div class="divider"></div>

  <section class="offers">
    <p><span class="free">FREE</span> ATMs</p>
    <p><span class="free">FREE</span> INSTALLATION</p>
    <p><span class="free">FREE</span> MAINTENANCE</p>
    <p class="no-cost">NO COST FOR BUSINESS OWNERS</p>
  </section>

  <section class="contact">
    <p class="contact-name">Ray T. Holbrook</p>
    <p class="contact-title">President · Owner</p>
    <div class="contact-details">
      <span>phone:</span><span>(555) 010-4477</span>
      <span>e-mail:</span><span>pqf.atm@zentromail.com</span>
      <span>address:</span><span>P.O. Box 87</span>
      <span></span><span>Hollow Pines, S.C. 29872</span>
    </div>
  </section>
</main>
</body>
</html>
```